Nutritionist and Personal Chef Services Flyer. My style is clean and contemporary.

I'm looking for a clean and stylish flyer that may or may not list my services and/or prices. These flyers will be featured in southern california (orange county and los angeles) fitness centers, wellness clinics, doctors offices, restaurants etc. so it has to be appropriate for any kind of facility. I want the concept design to be similar to my website:

www.verdantplatestudio.com

This is very important! Also, please see attached file to see what my header and business cards look like to keep style and formatting consistent.
Thanks so much!

The dimensions are going to be 5.5" by 8.5" vertical. I'd like it to be double-sided with a picture on one side and my information on the other side. For the photo side, I like the idea of having the picture of the hands and cutting board (fine for this to run horizontal). On the information side I need it to address the following:

1. I'd like to have a small photo of myself. I will upload which photo I want.
2. I want my header with my font and the kiwi exactly as is. Please see attachment and keep that formatting exactly.
3. Specialty Services:
Sports Nutrition
Weight-loss
Anti-aging and Detoxification
Cancer Prevention, Management and Survivorship
Children's Health and Wellness
Specialty Diets

4. My contact info:
Marisa Quenby, C.N. NC
949-555-0186
verdantplatestudio@mailvane.com

5. My website and the FB logo

6. Call or email me today to schedule a free 30-minute consultation.

```html
<!DOCTYPE html>
<html lang="en">
<head>
<meta charset="utf-8">
<title>Verdant Plate Studio – Flyer</title>
<link rel="stylesheet" href="https://fonts.googleapis.com/css2?family=Cinzel:wght@400&family=Cormorant+Garamond:wght@500&family=Lato:wght@400;700&family=Lora:wght@700&display=swap">
<style>
  :root{
    --backdrop:#e7e4df;
    --paper:#ffffff;
    --ink:#1a1a1a;
    --leaf:#7cb342;
    --leaf-soft:#8dc152;
    --band:#0c0c0c;
    --muted:#333333;
  }
  *{box-sizing:border-box;margin:0;padding:0}
  html,body{width:931px;height:1200px;overflow:hidden}
  body{background:var(--backdrop);font-family:"Lato",sans-serif;color:var(--ink);position:relative}
  .flyer{position:absolute;left:50px;top:20px;width:823px;height:1128px;background:var(--paper);overflow:hidden;box-shadow:0 2px 10px rgba(0,0,0,.25)}
  .artwork{position:absolute;inset:0}
  .brand{position:absolute;left:0;top:66px;width:670px;text-align:center}
  .brand-name{font-family:"Cinzel",serif;font-weight:400;font-size:35px;letter-spacing:.5px;color:#2a2a2a;line-height:1}
  .brand-tagline{font-family:"Cormorant Garamond",serif;font-weight:500;font-size:22px;color:#2a2a2a;margin-top:10px}
  .brand-mark{position:absolute;left:660px;top:80px;width:84px;height:84px;border-radius:50%;background:var(--leaf)}
  .info{position:absolute;left:250px;width:565px;text-align:center}
  .section-title{display:flex;align-items:center;justify-content:center;gap:10px;font-family:"Lora",serif;font-weight:700;font-size:27px;color:var(--leaf);line-height:1}
  .section-title::before,.section-title::after{content:"";width:72px;height:4px;background:var(--leaf);margin-top:12px}
  .section-text{font-size:13px;line-height:16px;color:var(--ink);margin-top:4px}
  .about{top:646px}
  .philosophy{top:729px}
  .philosophy .section-text{font-size:13.5px}
  .services{top:798px}
  .service-columns{position:absolute;left:318px;top:834px;width:490px;display:flex}
  .service-list{list-style:none;font-size:13px;line-height:15px}
  .service-list li{position:relative;padding-left:19px;margin-bottom:4px}
  .service-list li::before{content:"";position:absolute;left:0;top:6px;width:7px;height:3px;background:var(--leaf)}
  .service-list li::after{content:"";position:absolute;left:7px;top:3px;border-left:6px solid var(--leaf);border-top:4.5px solid transparent;border-bottom:4.5px solid transparent}
  .service-list.left{width:240px;padding-right:14px;border-right:1px solid #e3e3e3}
  .service-list.right{padding-left:20px}
  .contact{position:absolute;color:#fff}
  .contact-label{position:absolute;font-weight:700;font-size:25px;white-space:nowrap}
  .contact-label.contact-heading{left:308px;top:1018px}
  .contact-label.location-heading{left:272px;top:1070px}
  .contact-name{position:absolute;left:445px;top:1000px;font-size:20px;white-space:nowrap;display:flex;align-items:center;gap:6px}
  .phone-icon{width:20px;height:20px;background:var(--leaf);border-radius:3px;display:inline-flex;align-items:center;justify-content:center}
  .contact-phone{font-weight:700;font-size:23px}
  .contact-email{position:absolute;left:443px;top:1027px;font-size:18px;white-space:nowrap}
  .location-lines{position:absolute;left:400px;top:1057px;width:418px;text-align:center;font-size:18px;line-height:20.5px}
</style>
</head>
<body>
<main class="flyer">
  <svg class="artwork" width="823" height="1128" viewBox="0 0 823 1128">
    <defs>
      <linearGradient id="heroTone" x1="0" y1="0" x2="1" y2="1">
        <stop offset="0" stop-color="#d9472f"/>
        <stop offset=".3" stop-color="#9cc25a"/>
        <stop offset=".6" stop-color="#e9dcc6"/>
        <stop offset="1" stop-color="#c9b89a"/>
      </linearGradient>
    </defs>
    <!-- hero band -->
    <path role="img" aria-label="Hands slicing mushrooms on a cutting board with peppers, lettuce and sprouts" fill="url(#heroTone)"
      d="M0,222 C180,170 380,205 560,198 C700,192 780,172 823,160 L823,598 C700,612 520,560 340,572 C200,582 80,622 0,648 Z"/>
    <path d="M0,214 C180,162 380,197 560,190 C700,184 780,164 823,152" fill="none" stroke="var(--band)" stroke-width="14"/>
    <path d="M0,200 C180,148 380,183 560,176 C700,170 780,150 823,138" fill="none" stroke="var(--leaf)" stroke-width="8"/>
    <path d="M0,656 C80,630 200,590 340,580 C520,568 700,620 823,606" fill="none" stroke="var(--band)" stroke-width="14"/>
    <path d="M0,672 C80,646 200,606 340,596 C520,584 700,636 823,622" fill="none" stroke="var(--leaf)" stroke-width="6"/>
    <!-- footer band -->
    <path d="M0,1042 C250,992 520,968 823,960" fill="none" stroke="var(--leaf)" stroke-width="7"/>
    <path fill="var(--band)" d="M0,1060 C250,1010 520,986 823,978 L823,1128 L0,1128 Z"/>
    <!-- portrait circles -->
    <circle cx="155" cy="525" r="108" fill="var(--band)"/>
    <circle cx="155" cy="525" r="90" fill="var(--leaf)"/>
    <circle role="img" aria-label="Portrait of the chef in an apron in her kitchen" cx="155" cy="525" r="80" fill="#a89584"/>
    <circle cx="147" cy="798" r="100" fill="var(--band)"/>
    <circle cx="147" cy="798" r="84" fill="var(--leaf)"/>
    <circle role="img" aria-label="Black and white photo of an athletic back and shoulders" cx="147" cy="798" r="75" fill="#8a8a8a"/>
    <circle cx="140" cy="1020" r="92" fill="var(--band)"/>
    <circle cx="140" cy="1020" r="77" fill="var(--leaf)"/>
    <circle role="img" aria-label="Woman touching a screen of floating food icons" cx="140" cy="1020" r="69" fill="#b9c7cf"/>
  </svg>

  <header class="brand">
    <h1 class="brand-name">Verdant Plate Studio</h1>
    <p class="brand-tagline">Nutrition Designs | Personal Chef Services</p>
  </header>
  <div class="brand-mark"></div>

  <section class="info about">
    <h2 class="section-title">About</h2>
    <p class="section-text">I became aware of the joy of cooking in my grandmother's kitchen as a young child. In my mind, I will forever imagine her kitchen to smell of cinnamon-spiced apples, warm vanilla bean and buttery pie crust perfection.</p>
  </section>

  <section class="info philosophy">
    <h2 class="section-title">Philosophy</h2>
    <p class="section-text">Your body is the greatest instrument you'll ever own. It carries you through life. When you are good to your body, it shows.</p>
  </section>

  <section class="info services">
    <h2 class="section-title">Services by Design</h2>
  </section>
  <div class="service-columns">
    <ul class="service-list left">
      <li>Sports Nutrition</li>
      <li>Weight Loss</li>
      <li>Anti-Aging &amp; Anti-Inflammatory</li>
      <li>Cancer Prevention, Management &amp; Survivorship</li>
      <li>Detoxification</li>
    </ul>
    <ul class="service-list right">
      <li>Children's Health and Wellness</li>
      <li>Specialty Diets</li>
      <li>Services</li>
      <li>Nutrition Services</li>
      <li>Personal Chef Services</li>
    </ul>
  </div>

  <footer class="contact">
    <span class="contact-label contact-heading">Contact -</span>
    <span class="contact-name">Marisa Quenby
      <span class="phone-icon"><svg width="13" height="13" viewBox="0 0 24 24"><path fill="#111" d="M6.6 10.8a15.1 15.1 0 0 0 6.6 6.6l2.2-2.2c.3-.3.7-.4 1-.2 1.1.4 2.3.6 3.6.6.6 0 1 .4 1 1V20c0 .6-.4 1-1 1A17 17 0 0 1 3 4c0-.6.4-1 1-1h3.5c.6 0 1 .4 1 1 0 1.3.2 2.5.6 3.6.1.3 0 .7-.2 1z"/></svg></span>
      <span class="contact-phone">949.555.0186</span>
    </span>
    <span class="contact-email">verdantplatestudio@mailvane.com</span>
    <span class="contact-label location-heading">Location -</span>
    <p class="location-lines">Orange County &amp; select areas of Los Angeles.<br>Contact for specialty services of Los Angeles.<br>Contact for specialty services</p>
  </footer>
</main>
</body>
</html>
```